Stationary Package for Construction Company
Harborline Construction & Development, LLC
Stationary Package for Construction Company - Construction
Creative Brief
Bright & Fun-filled
Kevin R. Tolliver
Partner
1587 Marlow Avenue, STE 210 Myrtle Beach, SC 29577
kevin@harborlinehomebuilders.example
www.harborlinehomebuilders.example
travelkq travelkq

```html
<!DOCTYPE html>
<html lang="en">
<head>
<meta charset="utf-8">
<title>Harborline Construction &amp; Development — Business Card</title>
<link rel="stylesheet" href="https://fonts.googleapis.com/css2?family=Montserrat:wght@400;500;600&family=Open+Sans:wght@400;600&display=swap">
<style>
  :root {
    --backdrop: #8f8f8f;
    --card-white: #ffffff;
    --card-black: #141414;
    --brand-red: #d9282f;
    --peach: #f6c4b4;
    --ink: #3a3a3a;
    --ink-soft: #6b6b6b;
    --logo-grey: #3c3c3c;
    --back-text: #e8e8e8;
  }
  * { box-sizing: border-box; margin: 0; padding: 0; }
  html, body { width: 1200px; height: 900px; overflow: hidden; }
  body {
    background: var(--backdrop);
    font-family: "Open Sans", Arial, sans-serif;
    position: relative;
  }
  .card {
    position: absolute;
    left: 250px;
    width: 700px;
    height: 400px;
    border-radius: 18px;
    overflow: hidden;
    box-shadow: 0 10px 30px rgba(0,0,0,0.25);
  }
  .card-front { top: 30px; background: var(--card-white); }
  .card-back { top: 470px; background: var(--card-black); }

  .front-decoration {
    position: absolute;
    left: -90px;
    top: 150px;
    width: 380px;
    height: 380px;
    border-radius: 50%;
    background: var(--peach);
    opacity: 0.55;
  }
  .wordmark {
    display: flex;
    align-items: center;
    gap: 12px;
    font-family: "Montserrat", Arial, sans-serif;
  }
  .wordmark-dot {
    width: 34px; height: 34px;
    border-radius: 50%;
    background: var(--brand-red);
    flex-shrink: 0;
  }
  .wordmark-name {
    font-weight: 500;
    letter-spacing: 0.22em;
    color: var(--logo-grey);
  }
  .wordmark-tagline {
    font-size: 8px;
    letter-spacing: 0.16em;
    color: var(--ink-soft);
    margin-top: 3px;
    font-family: "Montserrat", Arial, sans-serif;
  }
  .front-logo { position: absolute; left: 330px; top: 46px; }
  .front-logo .wordmark-name { font-size: 26px; }

  .contact {
    position: absolute;
    left: 330px;
    top: 140px;
    font-size: 13px;
    color: var(--ink);
    line-height: 1.45;
  }
  .contact-address { margin-bottom: 12px; }
  .contact-list { list-style: none; }
  .contact-list li { display: flex; align-items: center; gap: 9px; }
  .contact-list svg { width: 12px; height: 12px; fill: var(--brand-red); flex-shrink: 0; }
  .contact-web { color: var(--brand-red); }

  .person { position: absolute; left: 40px; bottom: 50px; font-family: "Montserrat", Arial, sans-serif; }
  .person-name { font-size: 24px; font-weight: 500; color: var(--brand-red); }
  .person-title { font-size: 13px; color: var(--ink-soft); margin-top: 2px; }

  .back-logo {
    position: absolute;
    left: 0; right: 0; top: 120px;
    display: flex; justify-content: center;
  }
  .back-logo .wordmark-dot { width: 64px; height: 64px; }
  .back-logo .wordmark-name { font-size: 42px; color: #4a4a4a; }
  .back-logo .wordmark-tagline { font-size: 11px; color: #9a9a9a; }
  .back-web {
    position: absolute;
    left: 0; right: 0; bottom: 70px;
    text-align: center;
    color: var(--back-text);
    font-size: 17px;
    letter-spacing: 0.08em;
  }
</style>
</head>
<body>

<section class="card card-front">
  <div class="front-decoration" aria-hidden="true"></div>

  <div class="wordmark front-logo">
    <span class="wordmark-dot"></span>
    <div>
      <div class="wordmark-name">HARBORLINE</div>
      <div class="wordmark-tagline">CONSTRUCTION AND DEVELOPMENT</div>
    </div>
  </div>

  <div class="contact">
    <p class="contact-address">1587 Marlow Avenue, STE 210<br>Myrtle Beach, SC 29577</p>
    <ul class="contact-list">
      <li><svg viewBox="0 0 12 12"><path d="M2 1h2.5l1 2.5-1.3 1a6 6 0 0 0 3.3 3.3l1-1.3 2.5 1V11c-5 0-9-4-9-9z"/></svg>843.555.0142</li>
      <li><svg viewBox="0 0 12 12"><rect x="3" y="0.5" width="6" height="11" rx="1"/></svg>843.555.0187</li>
      <li><svg viewBox="0 0 12 12"><rect x="0.5" y="4" width="11" height="7" rx="1"/><rect x="3" y="1" width="6" height="3"/></svg>866.555.0163</li>
      <li><svg viewBox="0 0 12 12"><rect x="0.5" y="2" width="11" height="8" rx="1"/></svg>kevin@harborlinehomebuilders.example</li>
      <li class="contact-web"><svg viewBox="0 0 12 12"><circle cx="6" cy="6" r="5.5"/></svg>www.harborlinehomebuilders.example</li>
    </ul>
  </div>

  <div class="person">
    <div class="person-name">Kevin R. Tolliver</div>
    <div class="person-title">Partner</div>
  </div>
</section>

<section class="card card-back">
  <div class="wordmark back-logo">
    <span class="wordmark-dot"></span>
    <div>
      <div class="wordmark-name">HARBORLINE</div>
      <div class="wordmark-tagline">CONSTRUCTION AND DEVELOPMENT</div>
    </div>
  </div>
  <p class="back-web">www.harborlinehomebuilders.example</p>
</section>

</body>
</html>
```